Harlow Custom Craft Website update

I would like an updated website to my current site (Harlowcraft.com).
I have an updated logo i would like to incorporate.
24 pages , would like to integrate videos of the boats (that i can upload later)

Target Market(s)

Professional and Commercial boat owners

Industry/Entity Type

Custom Boat Manufacturing

Coding

Coded - Design and coding required

Number of Pages Required

5+ page

Font styles to use
Serif

Requirements
Must have
• Easy to read, well laid-out, and video integration
Nice to have
• Fresh up to date look

```html
<!DOCTYPE html>
<html lang="en">
<head>
<meta charset="utf-8">
<title>Harlow Custom Craft</title>
<link rel="stylesheet" href="https://fonts.googleapis.com/css2?family=Exo+2:ital,wght@1,800;1,900&family=Poppins:wght@400;500;600;700&display=swap">
<style>
:root{
  --red:#c8202b;
  --navy:#0b3ea8;
  --dark:#1d1e24;
  --ink:#2a2a2e;
  --white:#ffffff;
  --line:#d9dbe0;
}
*{margin:0;padding:0;box-sizing:border-box}
html,body{width:1200px;height:3561px;overflow:hidden}
body{position:relative;background:var(--white);font-family:"Poppins",sans-serif;color:var(--ink)}
.abs{position:absolute}
.display{font-family:"Exo 2",sans-serif;font-style:italic;font-weight:900;text-transform:uppercase;letter-spacing:-.5px}
.btn{position:absolute;display:flex;align-items:center;justify-content:center;font-size:11px;font-weight:600;text-transform:uppercase;color:var(--white);background:var(--navy);border-radius:0 34px 0 0;text-decoration:none}
.btn--ghost{background:transparent;border:1.5px solid var(--white)}

/* top bar + header */
.topbar{left:352px;top:0;width:848px;height:30px;background:linear-gradient(90deg,var(--red) 75%,#b9b9bd);clip-path:polygon(14px 0,100% 0,100% 100%,0 100%)}
.topbar span{position:absolute;top:8px;font-size:11px;color:var(--white);display:flex;align-items:center;gap:7px;white-space:nowrap}
.header{left:0;top:0;width:1200px;height:100px}
.brand{position:absolute;left:90px;top:36px;display:flex;align-items:center;gap:8px;font-size:19px;font-weight:700;color:var(--navy);white-space:nowrap}
.brand i{width:12px;height:12px;background:var(--red);display:block}
.nav{position:absolute;top:60px;font-size:11px;font-weight:600;text-transform:uppercase;color:var(--dark);white-space:nowrap}
.nav-contact{left:962px;top:44px;width:148px;height:44px}

/* hero */
.hero{left:0;top:100px;width:1200px;height:677px;background:linear-gradient(180deg,#8fa6b8 0%,#5f98a6 35%,#4b9aa0 60%,#3e7f8a 100%)}
.hero-boat{left:140px;top:140px;width:390px;height:410px;background:radial-gradient(ellipse at 50% 55%,#e8eef2 0%,#b8c6d2 45%,rgba(80,140,150,0) 72%)}
.hero-shade{left:0;top:0;width:1200px;height:677px;background:linear-gradient(90deg,rgba(0,0,0,0) 45%,rgba(30,40,70,.35))}
.play{position:absolute;border-radius:50%;background:var(--white);display:flex;align-items:center;justify-content:center}
.hero-title{left:691px;top:258px;font-size:52px;line-height:58px;color:var(--white)}
.hero-sub{left:692px;top:438px;width:420px;font-size:14px;line-height:20px;color:var(--white)}
.hero-mark{left:0;top:470px;width:1200px;font-size:250px;line-height:1;color:rgba(255,255,255,.12);text-align:center}

/* boat cards */
.card{position:absolute;top:679px;width:257px;height:296px;background:#2f6fa8}
.card .photo{position:absolute;left:0;top:0;width:100%;bottom:51px}
.card .label{position:absolute;left:0;bottom:0;width:100%;height:51px;background:#202125;color:var(--white);font-size:11px;font-weight:600;text-transform:uppercase;display:flex;align-items:center;justify-content:center}
.card--active{top:629px;height:346px}
.card--active .label{background:var(--red)}

/* about */
.about-title{left:90px;top:1082px;font-size:36px;color:var(--navy)}
.about-title em{color:var(--red);font-style:inherit}
.about-text{left:89px;top:1130px;width:505px;font-size:14.2px;line-height:19.6px;color:#333}
.about-text p+p{margin-top:5px}
.pic{position:absolute}

/* partners */
.badge{position:absolute;top:1602px;width:110px;height:100px}
.badge-box{left:571px;top:1591px;width:171px;height:122px;border:1.5px solid #333}

/* band */
.band{left:0;top:1812px;width:1200px;height:483px;background:linear-gradient(90deg,#4b5f6e 0%,#34434f 45%,#2f3742 100%)}
.band-photo{left:0;top:0;width:640px;height:483px;background:linear-gradient(180deg,#6d8090 0%,#3b5566 55%,#22384a 100%)}
.band-title{left:670px;top:1912px;font-size:36px;color:var(--white)}
.band-title em{color:var(--red);font-style:inherit}
.band-text{left:670px;top:1960px;width:424px;font-size:14.2px;line-height:19.6px;color:#eef0f4}

/* slider */
.ghost-mark{left:0;top:2320px;width:1200px;text-align:center;font-size:240px;line-height:1;color:#f2f3f5}
.slider-title{left:0;top:2390px;width:1200px;text-align:center;font-size:35px;color:var(--dark)}
.slider-title em{color:var(--red);font-style:inherit}
.nav-dot{position:absolute;width:30px;height:30px;border-radius:50%;display:flex;align-items:center;justify-content:center;color:var(--white);font-size:13px}
.counter{position:absolute;font-size:10px;color:#333;display:flex;align-items:center;gap:6px}
.counter b{font-weight:500;border:1px solid #333;border-radius:10px;padding:0 6px}

/* cta */
.footer{left:0;top:3076px;width:1200px;height:485px;background:var(--dark)}
.cta{left:88px;top:2961px;width:1022px;height:226px;background:linear-gradient(90deg,rgba(200,32,43,.93),rgba(214,62,72,.9));border-radius:0 0 260px 0 / 0 0 226px 0}
.cta-title{left:88px;top:3008px;width:1022px;text-align:center;font-size:34px;line-height:40px;color:var(--white)}
.col-title{position:absolute;top:3262px;font-family:"Exo 2",sans-serif;font-style:italic;font-weight:800;font-size:17px;color:var(--white);white-space:nowrap}
.links{position:absolute;left:419px;top:3295px;list-style:none;font-size:12px;font-weight:600;line-height:22.5px;color:#e6e7ea;width:140px}
.contact-row{position:absolute;left:618px;font-size:12px;font-weight:600;color:var(--white);display:flex;gap:12px;line-height:18px}
.contact-row u{text-decoration:underline}
.foot-brand{left:119px;top:3326px;width:280px;font-size:21px;font-weight:700;color:var(--white);display:flex;align-items:center;gap:9px;white-space:nowrap}
.foot-brand i{display:block;width:13px;height:13px;background:var(--white)}
.foot-about{left:119px;top:3385px;width:240px;font-size:11.5px;line-height:18px;color:#d8d9dd}
.sub-text{left:867px;top:3298px;width:230px;font-size:12px;font-weight:600;line-height:16px;color:var(--white)}
.sub-field{left:867px;top:3346px;width:210px;height:24px;border-bottom:1px solid #5a5c63;font-size:9px;letter-spacing:2px;color:#aaa}
.rule{left:0;top:3507px;width:1200px;height:1px;background:#3a3c43}
.copy{left:0;top:3526px;width:1200px;text-align:center;font-size:12px;color:#e6e7ea}
</style>
</head>
<body>

<!-- header -->
<div class="abs header">
  <div class="brand"><i></i>Harlow Custom Craft</div>
  <span class="nav" style="left:330px"><svg width="14" height="13" viewBox="0 0 14 13"><path d="M7 0 0 6h2v7h4V9h2v4h4V6h2z" fill="#0b3ea8"/></svg></span>
  <span class="nav" style="left:362px">Our Boats &#8964;</span>
  <span class="nav" style="left:453px">Optional Equipment</span>
  <span class="nav" style="left:599px">US Coast Guard Package</span>
  <span class="nav" style="left:777px">Driving Directions</span>
  <span class="nav" style="left:917px">Links</span>
  <a class="btn nav-contact">Contact Us</a>
</div>
<div class="abs topbar">
  <span style="left:39px"><svg width="9" height="12" viewBox="0 0 9 12"><path d="M4.5 0a4.5 4.5 0 0 0-4.5 4.5C0 8 4.5 12 4.5 12S9 8 9 4.5A4.5 4.5 0 0 0 4.5 0zm0 6.3a1.8 1.8 0 1 1 0-3.6 1.8 1.8 0 0 1 0 3.6z" fill="#fff"/></svg>4820 Harbor Rd. Marlow, LA 70399 USA</span>
  <span style="left:274px"><svg width="12" height="9" viewBox="0 0 12 9"><path d="M0 0h12v9H0z" fill="#fff"/><path d="m0 0 6 5 6-5" fill="none" stroke="#c8202b"/></svg>Office@harlowcraft.com</span>
  <span style="left:533px"><svg width="11" height="11" viewBox="0 0 11 11"><path d="M2.2 0 4 2.6 2.8 4a7 7 0 0 0 4.2 4.2L8.4 7 11 8.8 9.6 11C4.5 11 0 6.5 0 1.4z" fill="#fff"/></svg>(555) 201-4870</span>
  <span style="left:659px"><svg width="11" height="11" viewBox="0 0 11 11"><path d="M2.2 0 4 2.6 2.8 4a7 7 0 0 0 4.2 4.2L8.4 7 11 8.8 9.6 11C4.5 11 0 6.5 0 1.4z" fill="#fff"/></svg>(555) 201-4876</span>
</div>

<!-- hero -->
<section class="abs hero">
  <div class="abs hero-boat" role="img" aria-label="White twin-engine dive boat anchored in clear turquoise water"></div>
  <div class="abs hero-shade"></div>
  <div class="abs hero-mark display">Harlow</div>
  <div class="play" style="left:343px;top:221px;width:96px;height:96px"><svg width="26" height="30" viewBox="0 0 26 30"><path d="M0 0 26 15 0 30z" fill="#111"/></svg></div>
</section>
<h1 class="abs display hero-title">Custom Built<br>Boats. Proven<br>On The Water</h1>
<p class="abs hero-sub">Commercial aur Professional boat owners ke liye reliable, powerful aur customizable solutions.</p>
<a class="btn" style="left:693px;top:499px;width:147px;height:44px">View Our Boats</a>
<a class="btn btn--ghost" style="left:859px;top:499px;width:148px;height:44px">View Our Boats</a>

<!-- boat cards -->
<div class="card" style="left:87px"><div class="photo" role="img" aria-label="42 foot dive boat on calm grey sea" style="background:linear-gradient(180deg,#c9d3dc,#8fa4b6)"></div><div class="label">42' Dive Special</div></div>
<div class="card card--active" style="left:344px"><div class="photo" role="img" aria-label="36 and 46 foot dive boats docked at marina" style="background:linear-gradient(180deg,#6d9ad0,#d7dde4 60%,#5a7da8)"></div><div class="label">36' &amp; 46' Dive Specials</div></div>
<div class="card" style="left:602px"><div class="photo" role="img" aria-label="Divers on the stern platform of a 46 foot dive boat" style="background:linear-gradient(180deg,#5a93d6,#9fb7cc 55%,#3b6da0)"></div><div class="label">46' Dive Special</div></div>
<div class="card" style="left:856px"><div class="photo" role="img" aria-label="46 foot custom tour boat on deep blue water" style="background:linear-gradient(180deg,#4d7fb6,#1f4f93)"></div><div class="label">46' Custom Tour Boat</div></div>
<svg class="abs" style="left:1131px;top:854px" width="40" height="22" viewBox="0 0 40 22"><path d="M0 11h38M28 1l10 10-10 10" fill="none" stroke="#c8202b" stroke-width="2"/></svg>

<!-- about -->
<h2 class="abs display about-title">About <em>Us</em></h2>
<div class="abs about-text">
  <p>Our Harlow Dive Specials are especially designed for dive operators and dive enthusiasts alike. From our custom dive tank holders, water entry platforms, camera tables, fresh water rinse-downs, ample deck space and much, much more, you will see why our dive boats are making waves in the dive industry and are the number one requested boats by both divers and charter operators!</p>
  <p>Whether you are looking for a Charter Fish boat or looking to fulfill your dream of owning your own personal Fishing boat, our Harlow Sport Fish is your answer. We custom build all our boats to suit your needs and desires. We can build it simple or upgrade it to a yacht finish. We can install the electronics of your choice from the latest radars to the most sophisticated depth finders. The possibilities are limitless.</p>
</div>
<a class="btn" style="left:88px;top:1398px;width:129px;height:45px">Read More</a>
<div class="pic" role="img" aria-label="White flybridge cruiser docked in harbor" style="left:653px;top:1066px;width:248px;height:316px;background:linear-gradient(180deg,#7fa5c8,#dfe4ea 55%,#6f8ea6)"></div>
<div class="pic" role="img" aria-label="Blue hulled boat tied up at a pier" style="left:853px;top:1119px;width:229px;height:310px;border:4px solid #fff;background:linear-gradient(180deg,#3aa0d8,#b7d7e6 40%,#2e6e9c)"></div>
<div class="pic" role="img" aria-label="Center console boat running across the water" style="left:699px;top:1311px;width:182px;height:174px;border:4px solid #fff;background:linear-gradient(180deg,#5f7a5a,#cfd6db 55%,#8aa0ae)"></div>
<div class="play" style="left:930px;top:1245px;width:64px;height:64px"><svg width="16" height="18" viewBox="0 0 16 18"><path d="M0 0 16 9 0 18z" fill="#111"/></svg></div>

<!-- partners -->
<div class="badge" style="left:85px"><svg width="120" height="100" viewBox="0 0 120 100"><rect x="2" y="20" width="116" height="60" rx="8" fill="#6d9a3a"/></svg></div>
<div class="badge" style="left:265px"><svg width="100" height="100" viewBox="0 0 100 100"><circle cx="50" cy="50" r="46" fill="#3a8fc9"/></svg></div>
<div class="badge" style="left:437px"><svg width="100" height="100" viewBox="0 0 100 100"><circle cx="50" cy="50" r="44" fill="#1f2b44"/></svg></div>
<div class="abs badge-box"><svg width="168" height="119" viewBox="0 0 168 119"><rect x="34" y="20" width="100" height="78" rx="6" fill="#c8202b"/></svg></div>
<div class="badge" style="left:762px"><svg width="130" height="100" viewBox="0 0 130 100"><circle cx="65" cy="50" r="44" fill="#e98a2a"/></svg></div>
<div class="badge" style="left:935px"><svg width="126" height="100" viewBox="0 0 126 100"><ellipse cx="63" cy="50" rx="60" ry="44" fill="#2f4f8f"/></svg></div>

<!-- band -->
<section class="abs band">
  <div class="abs band-photo" role="img" aria-label="Large superyacht cruising past a wooded coastline"></div>
</section>
<h2 class="abs display band-title">Harlow <em>Craft</em></h2>
<p class="abs band-text">uses the latest technology and only the highest quality materials to build our custom boats. Our ongoing commitment to quality and customer satisfaction have helped us establish our position as a leader in custom boat industry. We attribute our growth to our commitment to excellence. We believe the commitment is essential for our continued success and growth. Our company provides quality custom boats that exceed our customers expectations.</p>
<a class="btn" style="left:670px;top:2137px;width:128px;height:47px">Read More</a>

<!-- slider -->
<div class="abs ghost-mark display">Harlow</div>
<h2 class="abs display slider-title">Check Out Our <em>71' Custom Dive</em></h2>
<div class="pic" role="img" aria-label="Dark hulled motor yacht on open water" style="left:198px;top:2485px;width:193px;height:337px;background:linear-gradient(90deg,#e0e3e6,#3e5566 55%,#1b2f45)"></div>
<div class="pic" role="img" aria-label="Sailing yacht anchored before green hills" style="left:391px;top:2454px;width:390px;height:401px;background:linear-gradient(180deg,#8fa6bf,#6f8a7a 45%,#3d7fb7 75%,#1f5d99)"></div>
<div class="pic" role="img" aria-label="Turquoise boat bow at sunset" style="left:781px;top:2485px;width:192px;height:337px;background:linear-gradient(90deg,#545b63,#d9d6d1 50%,#3f9fbf)"></div>
<div class="nav-dot" style="left:376px;top:2638px;background:var(--navy)">&#8249;</div>
<div class="nav-dot" style="left:766px;top:2638px;background:var(--red)">&#8250;</div>
<div class="play" style="left:554px;top:2621px;width:64px;height:64px"><svg width="16" height="18" viewBox="0 0 16 18"><path d="M0 0 16 9 0 18z" fill="#111"/></svg></div>
<div class="counter" style="left:326px;top:2836px"><b>44/86</b></div>
<div class="counter" style="left:798px;top:2836px">- <b>10 Sec</b> +</div>

<!-- cta + footer -->
<footer class="abs footer"></footer>
<div class="abs cta" role="img" aria-label="Boats moored in a marina under a red tint"></div>
<h2 class="abs display cta-title">Can’t Find What You’re Looking For?<br>Let’s Build It Together!</h2>
<a class="btn" style="left:520px;top:3101px;width:148px;height:46px">Contact Us</a>

<div class="abs foot-brand"><i></i>Harlow Custom Craft</div>
<p class="abs foot-about">Lorem ipsum dolor sit amet, consectetur adipiscing elit, sed do eiusmod tempor incid idunt ut labore et dolore magna aliqua.</p>

<div class="col-title" style="left:419px">Quick Links</div>
<ul class="links">
  <li>Home</li><li>Our Boats</li><li>Optional Equipment</li><li>US Coast Guard Package</li><li>Driving Directions</li><li>Links</li><li>Contact Us</li>
</ul>

<div class="col-title" style="left:618px">Contact Us</div>
<div class="contact-row" style="top:3293px"><svg width="11" height="11" viewBox="0 0 11 11"><path d="M2.2 0 4 2.6 2.8 4a7 7 0 0 0 4.2 4.2L8.4 7 11 8.8 9.6 11C4.5 11 0 6.5 0 1.4z" fill="#fff"/></svg>(555) 201-4870</div>
<div class="contact-row" style="top:3330px"><svg width="12" height="11" viewBox="0 0 12 11"><path d="M3 0h6v3H3zM0 4h12v5H9v2H3V9H0z" fill="#fff"/></svg><u>(555) 201-4876</u></div>
<div class="contact-row" style="top:3367px"><svg width="12" height="9" viewBox="0 0 12 9"><path d="M0 0h12v9H0z" fill="#fff"/><path d="m0 0 6 5 6-5" fill="none" stroke="#1d1e24"/></svg><u>Office@harlowcraft.com</u></div>
<div class="contact-row" style="top:3403px"><svg width="10" height="13" viewBox="0 0 9 12"><path d="M4.5 0a4.5 4.5 0 0 0-4.5 4.5C0 8 4.5 12 4.5 12S9 8 9 4.5A4.5 4.5 0 0 0 4.5 0zm0 6.3a1.8 1.8 0 1 1 0-3.6 1.8 1.8 0 0 1 0 3.6z" fill="#fff"/></svg><span>4820 Harbor Rd. Marlow,<br>LA 70399 USA</span></div>

<div class="col-title" style="left:867px">Subscribe for Updates</div>
<p class="abs sub-text">Subscribe and be the first to receive all the latest insights.</p>
<div class="abs sub-field">EMAIL</div>
<a class="btn" style="left:867px;top:3386px;width:148px;height:44px">Subscribe</a>

<div class="abs rule"></div>
<p class="abs copy">© 2025 Harlow Custom Craft Copyright © Reads All Rights Reserved.</p>

</body>
</html>
```